Quickset Remote Screening Lunch and Learn Event Flyer

We are hosting a lunch and learn for prospects to introduce our Digital Interview process - attendees are Human Resource and Hiring Managers.

We need a flyer that we can email and also have printed (large postcard size) to be either mailed out or dropped off at a prospects location. I have included a picture of a Digital Interview to be used on the flyer (people don't get it till they see it) as well as content. Please feel free to rewrite, restructure, the content to produce a good flow.

Return address on the back (the one we would print) is RL Staffing - 2740 Lorvane Court - Suite 318 - Nashville, TN 37490

Target Market(s)

Business Owners, Human Resource Managers

Industry/Entity Type

Digital

Font styles to use
Sans Serif

Requirements
Must have
• Must be clean and professional with plenty of white space

```html
<!DOCTYPE html>
<html lang="en">
<head>
<meta charset="UTF-8">
<title>Quickset Remote Screening – Benefits</title>
<link rel="stylesheet" href="https://fonts.googleapis.com/css2?family=Anton&family=Roboto:wght@300;400&display=swap">
<style>
  :root {
    --paper: #ffffff;
    --grey-light: #e3e3e3;
    --grey-soft: #eeeeee;
    --grey-mid: #cdcdcd;
    --red: #c4161c;
    --ink: #1a1a1a;
    --ink-soft: #555555;
    --star-a: #f6c343;
    --star-b: #e8902a;
  }
  html, body {
    margin: 0;
    padding: 0;
    overflow: hidden;
    background: var(--paper);
  }
  .flyer {
    position: relative;
    width: 854px;
    height: 1200px;
    overflow: hidden;
    background: var(--paper);
    font-family: "Roboto", Arial, sans-serif;
  }
  .backdrop {
    position: absolute;
    inset: 0;
  }
  .rule {
    position: absolute;
    height: 3px;
    background: var(--red);
  }
  .rule--top { top: 42px; left: 141px; right: 0; }
  .rule--bottom { top: 1148px; left: 35px; right: 0; }
  .benefits-title {
    position: absolute;
    left: 42px;
    top: 100px;
    margin: 0;
    font-family: "Anton", "Arial Black", sans-serif;
    font-weight: 400;
    font-size: 60px;
    line-height: 1;
    letter-spacing: 9px;
    color: var(--ink);
  }
  .title-bar {
    position: absolute;
    left: 304px;
    top: 145px;
    width: 508px;
    height: 13px;
    background: var(--red);
  }
  .benefit-list {
    position: absolute;
    left: 102px;
    top: 184px;
    margin: 0;
    padding: 0;
    list-style: none;
  }
  .benefit-item {
    display: flex;
    align-items: center;
    height: 43px;
    font-size: 29px;
    font-weight: 300;
    color: var(--ink);
    white-space: nowrap;
  }
  .benefit-item svg {
    width: 28px;
    height: 28px;
    margin-right: 4px;
    flex: none;
  }
  .intro {
    position: absolute;
    right: 36px;
    top: 622px;
    margin: 0;
    text-align: right;
    white-space: nowrap;
    font-size: 26px;
    font-weight: 300;
    line-height: 35.5px;
    color: var(--ink-soft);
  }
  .brand {
    position: absolute;
    right: 38px;
    top: 1094px;
    margin: 0;
    font-family: "Roboto", Arial, sans-serif;
    font-weight: 300;
    font-size: 28px;
    color: var(--ink);
  }
</style>
</head>
<body>
<main class="flyer">
  <svg class="backdrop" width="854" height="1200" viewBox="0 0 854 1200" aria-hidden="true">
    <polygon points="0,0 312,0 0,900" fill="var(--grey-light)"/>
    <polygon points="854,620 854,1200 330,1200" fill="var(--grey-soft)"/>
    <polygon points="0,880 500,1200 0,1200" fill="var(--grey-mid)"/>
  </svg>

  <div class="rule rule--top"></div>

  <h1 class="benefits-title">BENEFITS</h1>
  <div class="title-bar"></div>

  <svg width="0" height="0" style="position:absolute">
    <defs>
      <linearGradient id="star-fill" x1="0" y1="0" x2="0" y2="1">
        <stop offset="0" stop-color="var(--star-a)"/>
        <stop offset="1" stop-color="var(--star-b)"/>
      </linearGradient>
      <symbol id="star" viewBox="0 0 24 24">
        <polygon points="12,2 14.9,8.6 22,9.2 16.6,13.9 18.2,21 12,17.3 5.8,21 7.4,13.9 2,9.2 9.1,8.6" fill="url(#star-fill)" stroke="#c97a1e" stroke-width="0.8"/>
      </symbol>
    </defs>
  </svg>

  <ul class="benefit-list">
    <li class="benefit-item"><svg><use href="#star"/></svg>Lower Recruiting Costs</li>
    <li class="benefit-item"><svg><use href="#star"/></svg>Higher Quality Talent Pools</li>
    <li class="benefit-item"><svg><use href="#star"/></svg>Screen More Candidates in Less Time</li>
    <li class="benefit-item"><svg><use href="#star"/></svg>Schedule First Round Interviews with only Qualified</li>
    <li class="benefit-item"><svg><use href="#star"/></svg>Candidates</li>
    <li class="benefit-item"><svg><use href="#star"/></svg>Share with Multiple Hiring Managers</li>
    <li class="benefit-item"><svg><use href="#star"/></svg>Reduced Travel Expenses</li>
    <li class="benefit-item"><svg><use href="#star"/></svg>On Demand Flexibility</li>
  </ul>

  <p class="intro">Quickset Remote Screenings offer indi-<br>viduals the ability to share their stories and<br>demonstrate their work through video – all<br>on their own time by using a PC, Laptop, or<br>Smartphone. More than 60% of interviews<br>take place outside of the normal 9-5 business<br>hours. Learn how Hiring Managers can save<br>time, qualify more candidates, and can get a<br>better overall first impression before setting<br>up a first round interview.</p>

  <p class="brand">RL Staffing</p>

  <div class="rule rule--bottom"></div>
</main>
</body>
</html>
```